Digital Marketing Website Redesign, modern, fresh, dynamic

Hi there, we would like to freshen up our website and create a new dynamic look. We are a digital marketing agency who specialise in digital transformation in the form of creating websites for appointment bookings. Our clients are service businesses such as hairdressers, dentists and doctors who's patients need to book appointments with them.

Our company name is Plombek with the point being we can help increase your revenue curve by increasing your appointment bookings.

Our services include building the website, creating campaigns to drive traffic, increasing conversions and monitoring and reporting.

We are playing with a tagline of 'Step into your Digital Transformation' as we have a 5 step journey that customers can take with us getting them from zero to full appointment bookings.

Our current website is www.plomnbek-site.example

You can see a draft design that I mocked up on Canva here https://www.drawpadhub.example/design/QXT82LmnB7K/PoWz41kdRtGyvb_sxE_JNq/edit?utm_content=QXT82LmnB7K&utm_campaign=designshare&utm_medium=link2&utm_source=sharebutton

Also attached some other homepage ideas. In regard to photos we are open to ideas.

Please let if you need any more information to provide us with an initial design. Thanks million and I look forward to receiving fantastic designs :)

Marissa Tobler
Plombek

Target Market(s)

Appointment based businesses such as hairdressers, dentists, doctors

Industry/Entity Type

Marketing and Digital

Coding

Coded - Design and coding required

Number of Pages Required

1 page

Colors
0094D4
00A9DD
6FCCEA
C7EBF8
E9F6FB

Requirements
Must have
• Appointment booking CTA
Nice to have
• A website we like https://www.morwenhalbrook.example

```html
<!DOCTYPE html>
<html lang="en">
<head>
<meta charset="utf-8">
<title>Plombek – Step into your Digital Transformation</title>
<link href="https://fonts.googleapis.com/css2?family=Montserrat:wght@400;500;600;700&display=swap" rel="stylesheet">
<style>
:root{
  --blue:#0a90d2;
  --blue-bright:#00a9dd;
  --blue-soft:#6fccea;
  --blue-pale:#c7ebf8;
  --blue-mist:#e6f4fb;
  --lime:#c3cc10;
  --lime-dark:#a9b20c;
  --ink:#1c1c2a;
  --text:#3b3b48;
  --muted:#5d5d6a;
  --night:#14131f;
  --white:#ffffff;
  --card-line:#ececf0;
}
*{box-sizing:border-box;margin:0;padding:0}
html,body{width:1200px;height:3963px;overflow:hidden}
body{font-family:"Montserrat",sans-serif;color:var(--text);background:var(--white);position:relative}
.abs{position:absolute}
.btn{position:absolute;display:flex;align-items:center;justify-content:center;border-radius:22px;font-weight:600;font-size:15px;color:var(--white);box-shadow:-8px 0 0 var(--lime)}
.btn-blue{background:var(--blue)}
.btn-lime{background:var(--lime);box-shadow:-8px 0 0 var(--blue)}
.section-title{position:absolute;left:0;width:1200px;text-align:center;font-weight:700;font-size:34px;color:var(--blue)}
.section-title .accent{color:var(--blue)}

/* header */
.site-header{position:absolute;top:0;left:0;width:1200px;height:92px;background:var(--white)}
.brand{position:absolute;left:46px;top:24px;font-weight:700;font-size:34px;color:var(--blue)}
.brand-sub{position:absolute;left:190px;top:38px;font-size:12px;font-weight:600;color:var(--ink)}
.main-nav{position:absolute;left:505px;top:36px;display:flex;gap:20px;font-size:15px;color:var(--ink)}
.header-cta{left:941px;top:25px;width:210px;height:40px;font-size:15px}

/* hero */
.hero{position:absolute;top:92px;left:0;width:1200px;height:470px;overflow:hidden}
.hero-bg{position:absolute;inset:0;background:radial-gradient(ellipse 320px 260px at 780px 200px,#5fc4f0 0%,#1a6ea8 30%,#102447 60%,#0c1022 100%)}
.hero h1{position:absolute;left:111px;top:76px;font-size:34px;font-weight:600;line-height:41px;color:var(--white)}
.hero h1 span{color:var(--blue-bright)}
.hero p{position:absolute;left:111px;top:180px;width:500px;font-size:15.5px;line-height:28.5px;color:var(--white)}
.hero .ask{top:268px;left:114px;font-weight:600;font-size:16px}
.hero-cta{left:119px;top:320px;width:127px;height:42px}
.hero-wave{position:absolute;left:0;bottom:0}

/* testimonials */
.reviews{position:absolute;top:700px;left:111px;width:978px;display:flex;gap:18px}
.review{width:314px;height:269px;background:var(--white);border:1px solid var(--card-line);border-radius:6px;box-shadow:0 3px 12px rgba(0,0,0,.07);padding:36px 32px}
.review h3{font-size:17px;line-height:24px;font-weight:700;color:var(--blue)}
.stars{margin:26px 0 14px;font-size:12px;letter-spacing:1px;color:#f5c300}
.review p{font-size:15px;line-height:26px;color:var(--text)}
.authors{position:absolute;top:1000px;left:111px;display:flex;gap:0}
.author{width:332px;display:flex;align-items:center;gap:16px}
.avatar{width:66px;height:66px;border-radius:50%;border:3px solid var(--lime)}
.author b{display:block;font-size:15px;font-weight:600;color:var(--ink)}
.author small{font-size:13px;color:var(--muted)}

/* stats */
.stats{position:absolute;top:1161px;left:0;width:1200px;height:319px;background:var(--blue)}
.stat{position:absolute;width:220px;text-align:center;color:var(--white);font-size:19px;font-weight:600;line-height:26px}
.stat-ring{width:137px;height:137px;margin:0 auto 14px;border-radius:50%;background:var(--white);border:11px solid #7fc9ee;display:flex;align-items:center;justify-content:center;font-size:30px;font-weight:600;color:var(--ink)}

/* steps */
.steps{position:absolute;top:1669px;left:111px;display:flex;gap:18px}
.step{width:314px;height:266px;border-radius:6px;overflow:hidden;background:var(--white);box-shadow:0 3px 12px rgba(0,0,0,.08)}
.step-photo{height:162px}
.step-body{display:flex;align-items:center;gap:22px;padding:22px 26px}
.step-body span{font-size:20px;line-height:26px;font-weight:500;color:var(--ink)}
.arrow{position:absolute;width:32px;height:32px}

/* team */
.team{position:absolute;top:2063px;left:0;width:1200px;height:537px;background:var(--blue-mist)}
.team-title{position:absolute;left:114px;top:100px;font-size:34px;font-weight:700;color:var(--blue)}
.team-intro{position:absolute;left:369px;top:70px;width:720px;font-size:15.5px;line-height:28px;color:var(--text)}
.member{position:absolute;top:208px;width:240px;text-align:center}
.member .photo{width:172px;height:172px;border-radius:50%;margin:0 auto 22px;box-shadow:0 4px 14px rgba(0,0,0,.08)}
.member b{display:block;font-size:17px;font-weight:600;color:var(--ink);line-height:26px}
.member small{font-size:17px;color:var(--muted)}

/* pricing */
.plans{position:absolute;top:2792px;left:111px;display:flex;gap:18px}
.plan{position:relative;width:314px;height:436px;background:var(--white);border-radius:6px;box-shadow:0 3px 12px rgba(0,0,0,.08)}
.plan h3{height:72px;display:flex;align-items:center;justify-content:center;font-size:21px;font-weight:500;color:var(--ink)}
.price{height:77px;background:var(--blue-bright);display:flex;align-items:center;justify-content:center;color:var(--white);font-size:28px;font-weight:600}
.price small{font-size:19px;font-weight:400;margin-left:8px}
.price.lime{background:linear-gradient(90deg,var(--lime),var(--lime-dark))}
.plan-body{padding:22px 24px;font-size:15px;line-height:24px}
.plan-body b{display:block;color:var(--blue);font-size:19px;font-weight:600;margin-top:14px}
.plan-body b:first-child{margin-top:0}
.plan-body .plain{color:var(--ink);font-size:17px;font-weight:500}
.plan .btn{top:380px;left:32px;height:40px;font-size:15px}
.notes{position:absolute;top:3356px;left:0;width:1200px;text-align:center;font-size:15.5px;line-height:25px;color:var(--text)}

/* footer */
.site-footer{position:absolute;top:3430px;left:0;width:1200px;height:533px}
.footer-bg{position:absolute;left:0;top:0}
.footer-brand{position:absolute;top:188px;left:0;width:1200px;text-align:center;font-size:36px;font-weight:700;color:var(--white)}
.footer-nav{position:absolute;top:255px;left:0;width:1200px;display:flex;justify-content:center;gap:28px;font-size:16px;color:var(--white)}
.rule{position:absolute;left:111px;width:978px;height:1px;background:rgba(255,255,255,.25)}
.contact{position:absolute;top:340px;display:flex;gap:10px;color:var(--white);font-size:15px;line-height:26px}
.contact h4{font-size:16px;font-weight:600}
.copyright{position:absolute;top:491px;left:0;width:1200px;text-align:center;color:var(--white);font-size:15px}
</style>
</head>
<body>

<header class="site-header">
  <div class="brand">Plombek</div>
  <div class="brand-sub">Digital Transformation Consultancy</div>
  <nav class="main-nav"><span>5 steps</span><span>Our Pricing</span><span>Ahead of the Curve</span><span>Our Team</span></nav>
  <div class="btn btn-blue header-cta">Book an Appointment</div>
</header>

<section class="hero">
  <div class="hero-bg" role="img" aria-label="Person walking through a glowing futuristic digital tunnel"></div>
  <h1>Step into your<br><span>Digital Transformation</span></h1>
  <p>Digital transformation is a journey. At Plombek we divide the journey into five key steps that take your business from comprehensive market research to full appointment bookings.</p>
  <p class="ask">Ready to go on that journey?</p>
  <div class="btn btn-lime hero-cta">Start here</div>
  <svg class="hero-wave" width="1200" height="160" viewBox="0 0 1200 160">
    <path d="M0 62 C220 170 470 120 700 60 C900 10 1080 20 1200 80 L1200 160 L0 160Z" fill="#dfe48a"/>
    <path d="M0 70 C220 180 470 130 700 72 C900 22 1080 32 1200 100 L1200 160 L0 160Z" fill="var(--lime)"/>
    <path d="M0 80 C220 190 470 142 700 86 C900 38 1080 48 1200 118 L1200 160 L0 160Z" fill="var(--white)"/>
  </svg>
</section>

<h2 class="section-title" style="top:596px">Why Others Choose Us?</h2>

<div class="reviews">
  <article class="review"><h3>100 bookings in first month!</h3><div class="stars">★★★★★</div><p>Plombek’s booking system helped us get over 100 appointment bookings in May 2020.</p></article>
  <article class="review"><h3>From 55 new patients per month!</h3><div class="stars">★★★★★</div><p>Since Plombek optimised our marketing campaigns we’ve had 55-75 new patients per month.</p></article>
  <article class="review"><h3>25% increase in web traffic!</h3><div class="stars">★★★★★</div><p>Plombek have increased our Rankmeter ranking by 20,000 and our web traffic by 25%</p></article>
</div>
<div class="authors">
  <div class="author"><div class="avatar" role="img" aria-label="Portrait of Lucia Ferreira" style="background:linear-gradient(135deg,#e8c9b8,#9b6d5a)"></div><div><b>Lucia Ferreira</b><small>Owner, Shear &amp; Co</small></div></div>
  <div class="author"><div class="avatar" role="img" aria-label="Portrait of Dr. Min-Jae Oh" style="border-color:#ddd;background:linear-gradient(135deg,#d6d2cc,#6a4a36)"></div><div><b>Dr. Min-Jae Oh</b><small>Owner, Brightbite</small></div></div>
  <div class="author"><div class="avatar" role="img" aria-label="Portrait of Ludwig Hanner" style="border-color:#ddd;background:linear-gradient(135deg,#efe3d4,#b08a62)"></div><div><b>Ludwig Hanner</b><small>CEO, TokenPulse Watch</small></div></div>
</div>

<section class="stats">
  <div class="stat" style="left:83px;top:40px"><div class="stat-ring">726</div>Appointments<br>Booked</div>
  <div class="stat" style="left:356px;top:83px"><div class="stat-ring">31</div>Marketing<br>Campaigns</div>
  <div class="stat" style="left:629px;top:40px"><div class="stat-ring">25%</div>Website Traffic<br>Increase</div>
  <div class="stat" style="left:902px;top:83px"><div class="stat-ring"><svg width="56" height="28" viewBox="0 0 56 28"><path d="M28 14 C22 4 6 2 5 14 C6 26 22 24 28 14 C34 4 50 2 51 14 C50 26 34 24 28 14Z" fill="none" stroke="var(--ink)" stroke-width="3"/></svg></div>Creative Ideas</div>
</section>

<h2 class="section-title" style="top:1566px">Five Steps</h2>

<svg class="arrow" style="left:36px;top:1784px" viewBox="0 0 32 32"><circle cx="16" cy="16" r="14" fill="none" stroke="var(--blue)" stroke-width="2"/><path d="M19 9 L12 16 L19 23" fill="none" stroke="var(--blue)" stroke-width="2.5"/></svg>
<svg class="arrow" style="left:1131px;top:1784px" viewBox="0 0 32 32"><circle cx="16" cy="16" r="14" fill="none" stroke="var(--blue)" stroke-width="2"/><path d="M13 9 L20 16 L13 23" fill="none" stroke="var(--blue)" stroke-width="2.5"/></svg>

<div class="steps">
  <article class="step">
    <div class="step-photo" role="img" aria-label="Team planning a campaign at a whiteboard in an office" style="background:linear-gradient(135deg,#dfe3e6,#8a939b)"></div>
    <div class="step-body"><svg width="62" height="62" viewBox="0 0 62 62" fill="none" stroke="var(--blue)" stroke-width="2"><rect x="8" y="18" width="30" height="24" rx="3"/><rect x="28" y="6" width="24" height="20" rx="3"/><text x="13" y="36" font-size="14" fill="var(--blue)" stroke="none">#</text><circle cx="22" cy="52" r="6"/></svg><span>Creative<br>campaigns</span></div>
  </article>
  <article class="step">
    <div class="step-photo" role="img" aria-label="Desk with laptop, charts and research papers seen from above" style="background:linear-gradient(135deg,#b9a99a,#4f4a47)"></div>
    <div class="step-body"><svg width="62" height="62" viewBox="0 0 62 62" fill="none" stroke="var(--blue)" stroke-width="2"><rect x="30" y="30" width="6" height="18"/><rect x="40" y="20" width="6" height="28"/><rect x="50" y="10" width="6" height="38"/><circle cx="20" cy="34" r="10"/><path d="M13 41 L4 54"/></svg><span>Market<br>Research</span></div>
  </article>
  <article class="step">
    <div class="step-photo" role="img" aria-label="Smiling couple booking an appointment online at a laptop" style="background:linear-gradient(135deg,#efe7dc,#a37b58)"></div>
    <div class="step-body"><svg width="62" height="62" viewBox="0 0 62 62" fill="none" stroke="var(--blue)" stroke-width="2"><rect x="10" y="4" width="28" height="52" rx="4"/><path d="M18 28 L23 33 L32 22"/><circle cx="40" cy="40" r="8"/></svg><span>Online<br>Bookings</span></div>
  </article>
</div>
<div class="btn btn-blue" style="left:551px;top:1984px;width:107px;height:40px">Sign Up</div>

<section class="team">
  <h2 class="team-title">Our Team</h2>
  <p class="team-intro">From business management and web development to creative campaign delivery and social media expertise, our team has all the experience your business needs to it to the top of its digital game.</p>
  <svg class="arrow" style="left:34px;top:278px" viewBox="0 0 32 32"><circle cx="16" cy="16" r="14" fill="none" stroke="var(--blue)" stroke-width="2"/><path d="M19 9 L12 16 L19 23" fill="none" stroke="var(--blue)" stroke-width="2.5"/></svg>
  <svg class="arrow" style="left:1129px;top:278px" viewBox="0 0 32 32"><circle cx="16" cy="16" r="14" fill="none" stroke="var(--blue)" stroke-width="2"/><path d="M13 9 L20 16 L13 23" fill="none" stroke="var(--blue)" stroke-width="2.5"/></svg>
  <div class="member" style="left:79px"><div class="photo" role="img" aria-label="Portrait of Niamh" style="background:linear-gradient(160deg,#f2f2f2,#b08870)"></div><b>Niamh</b><small>Account Manager</small></div>
  <div class="member" style="left:347px"><div class="photo" role="img" aria-label="Portrait of Tomas" style="background:linear-gradient(160deg,#cfd6c4,#8a6b50)"></div><b>Tomas</b><small>Account Manager</small></div>
  <div class="member" style="left:614px"><div class="photo" role="img" aria-label="Portrait of Greta" style="background:linear-gradient(160deg,#f4f4f4,#b07a5c)"></div><b>Greta</b><small>Website specialist</small></div>
  <div class="member" style="left:881px"><div class="photo" role="img" aria-label="Portrait of Saoirse" style="background:linear-gradient(160deg,#c9b7a6,#23324f)"></div><b>Saoirse</b><small>Web developer</small></div>
</section>

<h2 class="section-title" style="top:2686px">Our Pricing</h2>

<div class="plans">
  <article class="plan">
    <h3>Starter Plan</h3>
    <div class="price">€399<small>/a month</small></div>
    <div class="plan-body"><b>Step 1:</b>Online readiness review based on our 12 point checklist<b>Step 2:</b>Implementation</div>
    <div class="btn btn-lime" style="width:144px;box-shadow:-8px 0 0 var(--blue)">Take 2 steps</div>
  </article>
  <article class="plan">
    <h3>Premium Plan</h3>
    <div class="price lime">€599<small>/a month</small></div>
    <div class="plan-body"><span class="plain">Steps 1 &amp; 2</span><b style="margin-top:22px">Step 3:</b>Content is King</div>
    <div class="btn btn-blue" style="width:151px">Take 3 steps</div>
  </article>
  <article class="plan">
    <h3>Ultimate Plan</h3>
    <div class="price">€899<small>/a month</small></div>
    <div class="plan-body"><span class="plain">Steps 1, 2 &amp; 3</span><b>Step 4:</b>Marketing Campaign<b>Step 5:</b>Monitor and Maintain</div>
    <div class="btn btn-lime" style="width:210px;box-shadow:-8px 0 0 var(--blue)">Take the full journey</div>
  </article>
</div>
<div class="btn btn-blue" style="left:468px;top:3275px;width:272px;height:40px">More info about the five steps</div>
<p class="notes">All plans include: Dedicated account manager - Minimum 3 months subscription<br>Marketing campaign can be implemented after one month - Additional activities charged at €65 per hour</p>

<footer class="site-footer">
  <svg class="footer-bg" width="1200" height="533" viewBox="0 0 1200 533">
    <path d="M0 45 C260 150 560 140 820 70 C980 28 1110 20 1200 40 L1200 533 L0 533Z" fill="var(--blue-soft)"/>
    <path d="M0 62 C260 170 560 160 820 92 C980 50 1110 42 1200 62 L1200 533 L0 533Z" fill="var(--blue)"/>
    <path d="M0 80 C260 190 560 182 820 116 C980 76 1110 68 1200 88 L1200 533 L0 533Z" fill="var(--night)"/>
  </svg>
  <div class="footer-brand">Plombek</div>
  <nav class="footer-nav"><span>5 steps</span><span>Our Pricing</span><span>Ahead of the Curve</span><span>Our Team</span></nav>
  <div class="rule" style="top:303px"></div>
  <div class="contact" style="left:111px">
    <svg width="20" height="24" viewBox="0 0 20 24" fill="none" stroke="#fff" stroke-width="1.8"><path d="M10 23 C4 15 2 11 2 8 A8 8 0 0 1 18 8 C18 11 16 15 10 23Z"/><circle cx="10" cy="8" r="3"/></svg>
    <div><h4>ADDRESS</h4>Northwest Innovation Campus,<br>Ardlow, Co. Donegal,<br>Ireland X00 A1B2</div>
  </div>
  <div class="contact" style="left:427px">
    <svg width="24" height="20" viewBox="0 0 24 20" fill="none" stroke="#fff" stroke-width="1.8"><rect x="1" y="2" width="22" height="16" rx="2"/><path d="M1 3 L12 11 L23 3"/></svg>
    <div><h4>EMAIL</h4>hello@plombek.example</div>
  </div>
  <div class="contact" style="left:621px">
    <svg width="22" height="22" viewBox="0 0 22 22" fill="none" stroke="#fff" stroke-width="1.8"><path d="M5 2 L9 7 L7 9 C8 12 10 14 13 15 L15 13 L20 17 L18 20 C10 20 2 12 2 4Z"/></svg>
    <div><h4>PHONE</h4>+353 1 555 0110</div>
  </div>
  <div class="contact" style="left:810px;font-size:14.5px">
    <svg width="22" height="22" viewBox="0 0 22 22" fill="none" stroke="#fff" stroke-width="1.8"><path d="M5 2 L9 7 L7 9 C8 12 10 14 13 15 L15 13 L20 17 L18 20 C10 20 2 12 2 4Z"/></svg>
    <div>General Enquiries: +353 1 555 0110<br>Customer Service: +353 1 555 0140<br>Investor Enquiries: +353 1 555 0160</div>
  </div>
  <div class="rule" style="top:465px"></div>
  <div class="copyright">2024 Plombek. All Rights Reserved.</div>
</footer>

</body>
</html>
```